Hexagon Honey Bottle Design, simple and elegant.

Bottle description:
BODY HEIGHT With cap 8.75cm
Without cap 8.6cm
DIAMETER Inner 4.4cm
Outer 5.2cm
Label height only has to be = 6cm height x (3.4X6) length of one hexagonal box is 3.4cm
See through bottle with black cap.
Concept of design:
Elegant, Simple, no pictures of bees, pictures of honeycomb, wooden honey stick, or drooling honey from either is ok. Simple colors. (Designer's discretion)
Wordings:
Hex1
Product of Yemen
Header:
KORVAL /MELO/ (Brand name)
Explanatory below header
Yemen Sidr Honey from The Valley Ra'ufil (100% Pure)
(name of honey)
250g
Optional
Hex2
Pure
=
No Additives (not even natural additives)
Hex3
Raw
=
Unheated, Unpasteurized, Unprocessed honey
Hex4
Natural
=
No added color, artificial flavor, or synthetic substance
Hex5
RENOWNED
=
Very well known by honey lovers
(Natural Pure Raw and Renowned) wordings to be on a suitable place on the bottle (maybe on the cap) -
Hex6
Imported By
The Lantern Bazaar Pte Ltd
No. 317, Cobalt Ferry Road, #09-12
Cobalt Ferry Plaza
Singapore 195340
Wordings can be rearranged - its up to the designer's discretion where and how to place them and in which order.-
Designer must be willing to do numerous changes as the design develops

```html
<!DOCTYPE html>
<html lang="en">
<head>
<meta charset="utf-8">
<title>Korval Melo – Hexagon Jar Label Set</title>
<link href="https://fonts.googleapis.com/css2?family=Raleway:wght@300;400;500&family=Crimson+Text:wght@400&display=swap" rel="stylesheet">
<style>
  :root {
    --page: #ffffff;
    --label-edge: #f6ebc6;
    --label-cream: #f8efcf;
    --label-glow: #fffdf5;
    --frame: #7a2c16;
    --badge-fill-light: #fff6dc;
    --badge-fill-deep: #ecd29a;
    --badge-ring: #6e2410;
    --text-soft: #8a6a3a;
    --text-deep: #4a2410;
  }
  * { box-sizing: border-box; margin: 0; padding: 0; }
  html, body {
    width: 1200px; height: 1200px; overflow: hidden;
    background: var(--page);
  }
  .label-sheet {
    width: 1200px; height: 1200px;
    display: flex; align-items: center; justify-content: center;
    gap: 14px;
  }
  .label {
    width: 182px; height: 320px;
    background: var(--label-edge);
    padding: 5px;
  }
  .label-frame {
    position: relative;
    width: 100%; height: 100%;
    border: 3px double var(--frame);
    overflow: hidden;
  }
  .label-ground {
    position: absolute; inset: 0;
    background:
      radial-gradient(ellipse 75% 42% at 50% 48%, var(--label-glow) 0%, rgba(255,253,245,0.85) 45%, rgba(255,253,245,0) 100%),
      linear-gradient(180deg, var(--label-cream) 0%, #fbf4dc 50%, var(--label-cream) 100%);
  }
  .badge {
    position: absolute;
    left: 50%; top: 64px;
    transform: translateX(-50%);
    width: 108px; height: 72px;
  }
  .badge svg { position: absolute; inset: 0; }
  .badge-word {
    position: absolute; inset: 0;
    display: flex; align-items: center; justify-content: center;
    font-family: "Raleway", sans-serif;
    font-weight: 400;
    color: var(--text-deep);
    font-size: 16px;
    letter-spacing: 0.5px;
    text-align: center;
    line-height: 1;
  }
  .badge-word.is-long { font-size: 13px; letter-spacing: 0.2px; }
  .brand-mark {
    position: absolute;
    left: 0; right: 0; top: 74px;
    text-align: center;
    font-family: "Raleway", sans-serif;
    font-weight: 400;
    color: var(--text-deep);
    font-size: 18px;
    letter-spacing: 1px;
    line-height: 1.05;
  }
  .label-copy {
    position: absolute;
    left: 6px; right: 6px;
    text-align: center;
    font-family: "Raleway", sans-serif;
    font-weight: 300;
    color: var(--text-soft);
    font-size: 9.5px;
    line-height: 1.35;
  }
  .label-copy.is-low { bottom: 48px; }
  .label-copy.is-main { bottom: 28px; }
  .label-copy.is-address { bottom: 30px; font-size: 8.5px; line-height: 1.55; }
  .honey-name {
    display: block;
    font-family: "Crimson Text", serif;
    font-size: 12.5px;
    color: var(--text-deep);
    margin: 6px 0 7px;
  }
  .net-weight { display: block; font-size: 9.5px; }
</style>
</head>
<body>
<main class="label-sheet">

  <section class="label label--brand">
    <div class="label-frame">
      <div class="label-ground" role="img" aria-label="Faint honeycomb pattern on cream ground"></div>
      <p class="brand-mark">KORVAL<br>MELO</p>
      <p class="label-copy is-main">
        Yemen Sidr Honey from The<br>Valley Ra'ufil<br>(100% Pure)
        <span class="honey-name">Name of Honey</span>
        <span class="net-weight">250g</span>
      </p>
    </div>
  </section>

  <section class="label label--pure">
    <div class="label-frame">
      <div class="label-ground" role="img" aria-label="Faint honeycomb pattern on cream ground"></div>
      <div class="badge">
        <svg viewBox="0 0 108 72" aria-hidden="true">
          <defs><radialGradient id="badgeFillA" cx="50%" cy="40%" r="65%"><stop offset="0" stop-color="#fff6dc"/><stop offset="1" stop-color="#ecd29a"/></radialGradient></defs>
          <rect x="3" y="6" width="102" height="60" rx="22" fill="url(#badgeFillA)" stroke="#6e2410" stroke-width="3"/>
          <rect x="9" y="11" width="90" height="50" rx="18" fill="none" stroke="#b8894a" stroke-width="1"/>
        </svg>
        <span class="badge-word">PURE</span>
      </div>
      <p class="label-copy is-low">No Additives<br>(not even natural additives)</p>
    </div>
  </section>

  <section class="label label--raw">
    <div class="label-frame">
      <div class="label-ground" role="img" aria-label="Faint honeycomb pattern on cream ground"></div>
      <div class="badge">
        <svg viewBox="0 0 108 72" aria-hidden="true">
          <defs><radialGradient id="badgeFillB" cx="50%" cy="40%" r="65%"><stop offset="0" stop-color="#fff6dc"/><stop offset="1" stop-color="#ecd29a"/></radialGradient></defs>
          <rect x="3" y="6" width="102" height="60" rx="22" fill="url(#badgeFillB)" stroke="#6e2410" stroke-width="3"/>
          <rect x="9" y="11" width="90" height="50" rx="18" fill="none" stroke="#b8894a" stroke-width="1"/>
        </svg>
        <span class="badge-word">RAW</span>
      </div>
      <p class="label-copy is-low">Unheated, Unpasteurized,<br>Unprocessed honey</p>
    </div>
  </section>

  <section class="label label--natural">
    <div class="label-frame">
      <div class="label-ground" role="img" aria-label="Faint honeycomb pattern on cream ground"></div>
      <div class="badge">
        <svg viewBox="0 0 108 72" aria-hidden="true">
          <defs><radialGradient id="badgeFillC" cx="50%" cy="40%" r="65%"><stop offset="0" stop-color="#fff6dc"/><stop offset="1" stop-color="#ecd29a"/></radialGradient></defs>
          <rect x="3" y="6" width="102" height="60" rx="22" fill="url(#badgeFillC)" stroke="#6e2410" stroke-width="3"/>
          <rect x="9" y="11" width="90" height="50" rx="18" fill="none" stroke="#b8894a" stroke-width="1"/>
        </svg>
        <span class="badge-word is-long">NATURAL</span>
      </div>
      <p class="label-copy is-low">No added color, artificial flavor<br>synthetic substance</p>
    </div>
  </section>

  <section class="label label--renowned">
    <div class="label-frame">
      <div class="label-ground" role="img" aria-label="Faint honeycomb pattern on cream ground"></div>
      <div class="badge">
        <svg viewBox="0 0 108 72" aria-hidden="true">
          <defs><radialGradient id="badgeFillD" cx="50%" cy="40%" r="65%"><stop offset="0" stop-color="#fff6dc"/><stop offset="1" stop-color="#ecd29a"/></radialGradient></defs>
          <rect x="3" y="6" width="102" height="60" rx="22" fill="url(#badgeFillD)" stroke="#6e2410" stroke-width="3"/>
          <rect x="9" y="11" width="90" height="50" rx="18" fill="none" stroke="#b8894a" stroke-width="1"/>
        </svg>
        <span class="badge-word is-long">RENOWNED</span>
      </div>
      <p class="label-copy is-low">Very well known by<br>honey lovers</p>
    </div>
  </section>

  <section class="label label--importer">
    <div class="label-frame">
      <div class="label-ground" role="img" aria-label="Faint honeycomb pattern on cream ground"></div>
      <p class="brand-mark">KORVAL<br>MELO</p>
      <p class="label-copy is-address">
        Imported By<br>
        The Lantern Bazaar Pte Ltd<br>
        No. 317, Cobalt Ferry Road, #09-12<br>
        Cobalt Ferry Plaza<br>
        Singapore 195340
      </p>
    </div>
  </section>

</main>
</body>
</html>
```